KVR Fashion Design Company Needs a New Web Design, Please Click Me

Designers:

PLEASE NOTE: we only need the web page design, not a fully coded website.

Our brand's name is The Amber Loft, our signature is print. our style is edgy and chic.

The old website is too messy. here's the address:
www.kvrstudio-example.com.cn

The new website's purpose is to show our brand/design and most importantly, sell products, So it should be a combination of a designer official website and online shopping. I want the whole style to be clean, edgy and pioneer, easy to understand. we need a sophisticated online shopping website.

The reference websites are:
lumorivet.co.uk
www.qd-pelm.com
dariustoke.com
belusarno.com
fenwirapadlos.com

Please beat their designs :)

Check out our lasted fashion show to get to know us more.

https://www.vidstreamexample.com/watch?v=ZtrmKqLwXbPo&spfreload=10

The attachments are our Logo and some 2015 Look Book.
(Please let us know if you want to play with our print in this particular web design, we can send the source file.)
Updates

Designers, we really like the design of marisolvantree.com(we have attached a picture of the website) , Can we get a homepage like that? so the designs you submit will be 3 pages. The first one should be a page that only has Shop/Look. then the shop page, it should be nothing but our product which we will list the categories ourself. And the look page should contain all the info. such as news, about us and designers etc. Thank you all for your hard work, we really enjoyed the designs. Added Monday, November 03, 2014

Target Market(s)

Our target audiences are woman aged from 16-40 who like online shopping

Industry/Entity Type

Online Shopping

Number of Pages Required

3 page

Font styles to use
Serif
Sans Serif
Script

Requirements
Must have
• Designers,
• we really like the design of marisolvantree.com(we have attached a picture of the website) , Can we get a homepage like that? so the designs you submit will be 3 pages. The first one should be a page that only has Shop/Look. then the shop page, it should be nothing but our product which we will list the categories ourself. And the look page should contain all the info. such as news, about us and designers etc. Thank you all for your hard work, we really enjoyed the designs.

```html
<!DOCTYPE html>
<html lang="en">
<head>
<meta charset="utf-8">
<title>KVR Group · The Amber Loft</title>
<link href="https://fonts.googleapis.com/css2?family=Playfair+Display:wght@400;700&family=Open+Sans:wght@400;600&display=swap" rel="stylesheet">
<style>
:root{
  --ink:#222;
  --dark:#2b2b2b;
  --mute:#777;
  --line:#ddd;
  --red:#c8161d;
  --paper:#fff;
  --soft:#f3f3f3;
}
*{margin:0;padding:0;box-sizing:border-box}
html,body{width:1200px;height:5149px;overflow:hidden}
body{position:relative;background:var(--paper);color:var(--ink);font-family:"Open Sans",Arial,sans-serif;font-size:12px}
.abs{position:absolute}
.serif{font-family:"Playfair Display",Georgia,serif}
.ph{position:absolute;overflow:hidden}
.topbar{left:0;top:0;width:1200px;height:31px;background:var(--dark);color:#ddd;font-size:11px;display:flex;justify-content:space-between;align-items:center;padding:0 158px}
.topbar .links span{margin-left:16px}
.brand{left:0;top:40px;width:1200px;text-align:center}
.brand .mark{width:52px;height:52px;border-radius:50%;background:var(--red);margin:0 auto 10px}
.brand .name{font-family:"Playfair Display",Georgia,serif;font-size:15px;letter-spacing:2px;line-height:18px;color:var(--ink)}
.nav{left:0;top:172px;width:1200px;display:flex;justify-content:center;gap:42px;font-size:11px;letter-spacing:1px}
.nav .on{color:var(--red);border-bottom:1px solid var(--red);padding-bottom:4px}
.mega{left:158px;top:200px;width:884px;height:234px;background:var(--paper);border:1px solid var(--line)}
.mega .col{position:absolute;top:30px;font-size:11px;line-height:22px;color:var(--mute)}
.mega .col b{display:block;color:var(--ink);font-weight:600;border-bottom:1px solid var(--line);margin-bottom:6px;width:130px}
.mega .tag{position:absolute;left:16px;bottom:16px;color:#fff;font-family:"Playfair Display",serif;font-size:20px;letter-spacing:1px}
.hero{left:0;top:434px;width:1200px;height:309px;background:linear-gradient(90deg,#f1f1f1,#fafafa 40%,#e4e4e4 70%,#f5f5f5)}
.hero .title{position:absolute;left:900px;top:108px;width:220px;font-family:"Playfair Display",serif;font-size:30px;line-height:32px;text-align:right;color:var(--ink)}
.arrow{position:absolute;top:140px;width:30px;height:30px;border-radius:50%;background:#444}
.btn{display:inline-block;font-size:10px;letter-spacing:1px;padding:9px 22px;text-transform:uppercase}
.btn.light{background:#fff;border:1px solid #333;color:var(--ink)}
.btn.red{background:var(--red);color:#fff}
.btn.dark{background:var(--dark);color:#fff}
.big{font-family:"Playfair Display",serif;font-size:56px;letter-spacing:3px;font-weight:400}
.copy{font-size:11px;line-height:18px;color:var(--mute)}
.h2{font-family:"Playfair Display",serif;font-size:36px;letter-spacing:1px}
.prod-label{font-size:10px;line-height:16px}
.news-date{font-size:9px;color:#999;text-align:center}
.news-title{font-family:"Playfair Display",serif;font-size:14px;line-height:18px;text-align:center;margin-top:10px}
.news-text{font-size:10px;line-height:15px;color:var(--mute);text-align:center;margin-top:8px}
.social{position:absolute;top:4730px;width:70px;text-align:center;font-size:10px;color:var(--mute)}
.social i{display:block;width:58px;height:58px;border-radius:50%;background:var(--dark);margin:0 auto 8px}
.footbar{left:0;top:5080px;width:1200px;height:69px;background:var(--dark);color:#aaa;font-size:10px;display:flex;justify-content:space-between;align-items:center;padding:0 40px}
.pay{display:inline-block;width:40px;height:18px;border-radius:3px;background:#777;margin-left:10px}
</style>
</head>
<body>

<div class="abs topbar">
  <span>Choose with Best &amp; Buy Stylish Shop</span>
  <span class="links"><span>Search</span><span>Register</span><span>Login</span><span>My Cart (0)</span><span>EN</span></span>
</div>

<header class="abs brand">
  <div class="mark"></div>
  <div class="name">KVR GROUP<br>THE AMBER LOFT</div>
</header>

<nav class="abs nav">
  <span>HOME</span><span class="on">ONLINE SHOPPING</span><span>ABOUT US</span><span>DESIGNERS</span><span>NEWS</span><span>MEMBER CENTER</span>
</nav>

<div class="abs mega">
  <div class="ph" role="img" aria-label="Menswear model in black suit" style="left:8px;top:30px;width:130px;height:188px;background:radial-gradient(ellipse 40% 55% at 50% 70%,#1c1c1e 0%,#3a3a3c 55%,rgba(58,58,60,0) 100%),linear-gradient(#f2f2f2,#d6d6d6)"></div>
  <div class="ph" role="img" aria-label="Womenswear model in green dress" style="left:146px;top:30px;width:130px;height:188px;background:radial-gradient(ellipse 38% 55% at 50% 68%,#1f6a45 0%,#2f7d55 50%,rgba(47,125,85,0) 100%),linear-gradient(#eef0ee,#cfd6d1)"></div>
  <div class="tag">THE AMBER LOFT</div>
  <div class="col" style="left:456px"><b>SHOP</b>New Fashion<br>New Products<br>Recommend<br>Fitting</div>
  <div class="col" style="left:594px"><b>CATEGORY</b>Men<br>Women</div>
  <div class="col" style="left:753px"><b>MY ACCOUNT</b>My Accounts<br>Shopping Cart<br>Track Your Order<br>Checkout + Pay</div>
</div>

<section class="abs hero">
  <div class="ph" role="img" aria-label="Monochrome double exposure of a woman's profile and a city skyline" style="left:130px;top:0;width:560px;height:309px;background:radial-gradient(ellipse 30% 60% at 18% 70%,#111 0%,#333 45%,rgba(60,60,60,0) 100%),radial-gradient(ellipse 45% 55% at 60% 45%,#8d8d8d 0%,#b9b9b9 50%,rgba(220,220,220,0) 100%),linear-gradient(90deg,#fff,#e8e8e8 50%,#f4f4f4)"></div>
  <div class="arrow" style="left:18px"></div>
  <div class="arrow" style="left:1152px"></div>
  <div class="title">IT'S<br>JUST THE<br>BEGINNING</div>
  <div class="abs" style="left:932px;top:232px"><span class="btn light">Shop Now</span></div>
</section>

<section class="abs" style="left:0;top:743px;width:1200px;height:697px">
  <div class="ph" role="img" aria-label="Male model in grey three-piece suit" style="left:0;top:0;width:600px;height:697px;background:radial-gradient(ellipse 30% 58% at 50% 70%,#2a2b2e 0%,#3c3d41 55%,rgba(60,61,65,0) 100%),radial-gradient(ellipse 9% 8% at 50% 16%,#c9a58b 0%,rgba(201,165,139,0) 100%),linear-gradient(#eeeeee,#d9d9d9)"></div>
  <div class="abs" style="left:700px;top:180px;width:400px;text-align:center">
    <div class="big">MEN</div>
    <p class="copy" style="margin-top:30px">Sharp tailoring cut for the modern city, refined lines in dark wool and clean white shirts for every day.</p>
    <p class="copy" style="margin-top:14px">Discover structured jackets, slim trousers and soft knits made to layer with ease.</p>
    <div style="margin-top:56px"><span class="btn red">Shop Now</span></div>
  </div>
</section>

<section class="abs" style="left:0;top:1440px;width:1200px;height:688px">
  <div class="abs" style="left:100px;top:150px;width:400px;text-align:center">
    <div class="big">WOMEN</div>
    <p class="copy" style="margin-top:30px">Bold prints and quiet shapes, pieces for women who dress with intent and move with confidence.</p>
    <p class="copy" style="margin-top:14px">New season coats, flowing skirts and crisp tops, ready to wear from day into night.</p>
    <div style="margin-top:56px"><span class="btn dark">Shop Now</span></div>
  </div>
  <div class="ph" role="img" aria-label="Female model in white coat and full skirt in a bright arched corridor" style="left:600px;top:0;width:600px;height:688px;background:radial-gradient(ellipse 32% 55% at 52% 68%,#ffffff 0%,#f4f4f2 50%,rgba(244,244,242,0) 100%),radial-gradient(ellipse 10% 8% at 50% 20%,#2a2a2a 0%,rgba(42,42,42,0) 100%),linear-gradient(90deg,#b9c8c7,#e6eceb 30%,#dfe6e5 70%,#a9b9b8)"></div>
</section>

<section class="abs" role="img" aria-label="Blurred city street in monochrome" style="left:0;top:2128px;width:1200px;height:659px;background:radial-gradient(ellipse 40% 60% at 80% 40%,#e4e4e4 0%,rgba(228,228,228,0) 100%),linear-gradient(90deg,#3a3a3a,#7a7a7a 35%,#a5a5a5 60%,#cfcfcf)"></section>
<div class="ph" role="img" aria-label="Model wearing printed dress" style="left:158px;top:2334px;width:206px;height:240px;background:radial-gradient(ellipse 40% 50% at 50% 65%,#5c2c6a 0%,#9a3d4f 45%,rgba(154,61,79,0) 100%),linear-gradient(#c9a284,#2c2630)"></div>
<div class="ph" role="img" aria-label="Model wearing blue printed outfit" style="left:388px;top:2334px;width:206px;height:240px;background:radial-gradient(ellipse 40% 55% at 50% 62%,#3f74c4 0%,#6f9ad8 45%,rgba(111,154,216,0) 100%),linear-gradient(#e3e6ea,#2b4a7e)"></div>
<div class="abs prod-label" style="left:158px;top:2584px;color:#eee">PRINTED GOWN<br>¥2,311</div>
<div class="abs prod-label" style="left:388px;top:2584px;color:#eee">PRINTED SUIT<br>¥2,311</div>
<div class="abs" style="left:614px;top:2348px;width:420px;color:#fff">
  <div class="h2" style="font-size:40px">NEW COLLECTIONS</div>
  <p style="font-size:11px;line-height:17px;margin-top:18px;color:#f2f2f2">Our latest collection brings signature prints into sharp silhouettes, mixing graphic colour with calm neutral bases for a look that feels both edgy and easy to wear.</p>
  <p style="font-size:11px;line-height:17px;margin-top:14px;color:#f2f2f2">Each piece is made in small runs, cut with care and finished by hand in our own studio workshop.</p>
</div>

<section class="abs" style="left:0;top:2787px;width:1200px;height:503px">
  <div class="abs" style="left:158px;top:70px;width:400px">
    <div class="h2">DESIGNERS</div>
    <p class="copy" style="margin-top:22px">Our designers come from many cities and schools, each bringing a personal point of view to the studio and shaping the voice of every new season.</p>
    <p class="copy" style="margin-top:12px">Meet the people behind the prints and learn how ideas move from sketch to finished garment.</p>
    <div style="margin-top:36px"><span class="btn dark">Read More</span></div>
  </div>
  <div class="ph" role="img" aria-label="Portrait of a female designer" style="left:614px;top:58px;width:198px;height:250px;background:radial-gradient(ellipse 45% 45% at 50% 85%,#111 0%,#2a2a2a 55%,rgba(42,42,42,0) 100%),radial-gradient(ellipse 28% 30% at 50% 38%,#1a1a1a 0%,rgba(26,26,26,0) 100%),linear-gradient(#f4f4f4,#dedede)"></div>
  <div class="ph" role="img" aria-label="Portrait of a designer duo" style="left:824px;top:58px;width:213px;height:250px;background:radial-gradient(ellipse 30% 45% at 30% 80%,#1d1d1d 0%,rgba(29,29,29,0) 100%),radial-gradient(ellipse 30% 45% at 72% 82%,#2b2b2b 0%,rgba(43,43,43,0) 100%),linear-gradient(#ededed,#cfcfcf)"></div>
  <div class="abs serif" style="left:614px;top:318px;width:198px;text-align:center;font-size:13px">Mira Solen</div>
  <div class="abs serif" style="left:824px;top:318px;width:213px;text-align:center;font-size:13px">Orin Vale</div>
</section>

<section class="abs" style="left:0;top:3290px;width:1200px;height:542px">
  <div class="abs h2" style="left:158px;top:0">FEATURED NEWS</div>
  <p class="abs copy" style="left:614px;top:0;width:423px;font-size:10px;line-height:15px">The latest stories from our studio, from shows and shop openings to new partners and events around the world.</p>
  <div class="ph" role="img" aria-label="Storefront at night with warm window light" style="left:158px;top:58px;width:278px;height:205px;background:radial-gradient(ellipse 50% 40% at 50% 60%,#b58a4f 0%,rgba(181,138,79,0) 100%),linear-gradient(#2c2c2c,#4d4437 60%,#6b5a44)"></div>
  <div class="ph" role="img" aria-label="Bright showroom interior with red floor" style="left:467px;top:58px;width:278px;height:205px;background:linear-gradient(#eef3f5 0%,#d6e0e4 45%,#c9785f 70%,#a23a2a)"></div>
  <div class="ph" role="img" aria-label="Event stage with guests under warm lights" style="left:760px;top:58px;width:277px;height:205px;background:radial-gradient(ellipse 45% 35% at 50% 35%,#b9937a 0%,rgba(185,147,122,0) 100%),linear-gradient(#4a3e37,#1f1b19)"></div>
  <div class="abs" style="left:158px;top:278px;width:278px">
    <div class="news-date">MAY 7, 2015</div>
    <div class="news-title">KVR Shanghai | pillars of fashion for tomorrow</div>
    <div class="news-text">A look at how our studio connects new talent with partners across two continents this year.</div>
  </div>
  <div class="abs" style="left:467px;top:278px;width:278px">
    <div class="news-date">MAY 7, 2015</div>
    <div class="news-title">KVR Shanghai | in ORBIS HOUSE fashion resources</div>
    <div class="news-text">Our latest pieces join a curated showroom of independent labels in the heart of the city.</div>
  </div>
  <div class="abs" style="left:760px;top:278px;width:277px">
    <div class="news-date">MARCH 29, 2015</div>
    <div class="news-title" style="color:var(--red)">March 29–30, with RENA couple together</div>
    <div class="news-text">Two evenings of music, prints and people, shared with friends of the house.</div>
  </div>
</section>

<section class="abs" role="img" aria-label="Blurred boutique interior" style="left:0;top:3832px;width:1200px;height:542px;background:radial-gradient(ellipse 30% 50% at 12% 40%,#e8e8e8 0%,rgba(232,232,232,0) 100%),radial-gradient(ellipse 30% 50% at 88% 55%,#cfcfcf 0%,rgba(207,207,207,0) 100%),linear-gradient(90deg,#5a5a5a,#9c9c9c 50%,#6e6e6e)"></section>
<div class="ph" role="img" aria-label="Fashion show video still of a lit shop front" style="left:297px;top:3967px;width:614px;height:330px;background:radial-gradient(ellipse 30% 45% at 72% 40%,#cdb48f 0%,rgba(205,180,143,0) 100%),radial-gradient(ellipse 25% 40% at 20% 45%,#8b8f96 0%,rgba(139,143,150,0) 100%),linear-gradient(#3c3c3e,#1e1e20)"></div>
<svg class="abs" style="left:564px;top:4092px" width="80" height="80" viewBox="0 0 80 80">
  <circle cx="40" cy="40" r="36" fill="rgba(0,0,0,0.25)" stroke="#fff" stroke-width="3"/>
  <path d="M32 24 L58 40 L32 56 Z" fill="#fff"/>
</svg>

<footer>
  <div class="abs brand" style="top:4450px">
    <div class="mark"></div>
    <div class="name">KVR GROUP<br>THE AMBER LOFT</div>
  </div>
  <p class="abs copy" style="left:158px;top:4600px;width:884px;text-align:center;font-size:10px;line-height:16px">KVR The Amber Loft is committed to giving young designers a stage, supporting the exchange of cultures, ideas and creative work, and making great design easy to find, wear and share with the people who love it.</p>
  <div class="social" style="left:415px"><i></i>Social A</div>
  <div class="social" style="left:565px"><i></i>Social B</div>
  <div class="social" style="left:715px"><i></i>Social C</div>
  <div class="abs footbar">
    <span>Copyright © 2015 The Amber Loft. All Rights Reserved.</span>
    <span><span class="pay"></span><span class="pay"></span></span>
  </div>
</footer>

</body>
</html>
```